MRHT Needs Fundraiser Dinner Invite!!

The Marisol Hendrick Trust, a 501 3(c) non for profit has a yearly fundraiser, with varying themes. Last year it was "cowboys" and "cowgirls"
This year, it is Club Orchid, or 70's disco music. I have uploaded last years invite for reference, some stock photography for inspiration. You are not limited to using the stock photos.

Annual MRHT Fundraiser Dinner
October 13th, 2022
Starts: 6:30pm
RSVP By: September 20th
Place: The Bramwell
Price: $135 per ticket

Target Market(s)

Donors, Business People, Every person

Industry/Entity Type

Non for Profit

Font styles to use
Sans Serif

Colors
0054AA
0677BA
7BADD7
CADEEF
E8F1F8
E54698
E96AAD
F1A4CE
F9D9EA
FCEFF6
6B429C
8869AF
B7A5CE
E3DAEB
F3F0F8

Requirements
Must have
• The invite should be 5x7, be sophisticated as the clientele are mainly business people that come to support the cause. It should be fun and inviting at the same time.

```html
<!DOCTYPE html>
<html lang="en">
<head>
<meta charset="utf-8">
<title>Annual MRHT Fundraiser Dinner</title>
<link rel="stylesheet" href="https://fonts.googleapis.com/css2?family=Monoton&family=Abril+Fatface&family=Archivo:wght@700&display=swap">
<style>
  :root {
    --blue-deep: #0054AA;
    --blue-mid: #0677BA;
    --blue-soft: #7BADD7;
    --blue-pale: #CADEEF;
    --blue-mist: #E8F1F8;
    --pink-hot: #E54698;
    --pink-mid: #E96AAD;
    --pink-soft: #F1A4CE;
    --pink-pale: #F9D9EA;
    --pink-mist: #FCEFF6;
    --purple-deep: #6B429C;
    --purple-mid: #8869AF;
    --purple-soft: #B7A5CE;
    --purple-pale: #E3DAEB;
    --white: #FFFFFF;
  }
  * { margin: 0; padding: 0; box-sizing: border-box; }
  html, body { width: 857px; height: 1200px; overflow: hidden; background: var(--blue-mist); }
  .invite {
    position: relative;
    width: 857px;
    height: 1200px;
    overflow: hidden;
    background:
      linear-gradient(155deg, rgba(255,255,255,0) 30%, rgba(252,239,246,0.75) 48%, rgba(255,255,255,0) 62%),
      linear-gradient(180deg, var(--purple-pale) 0%, var(--pink-mist) 30%, var(--blue-pale) 52%, var(--blue-soft) 78%, #9CC0E2 100%);
  }
  .illustration {
    position: absolute;
    left: 420px;
    top: 0;
    width: 437px;
    height: 1200px;
    background:
      radial-gradient(circle at 72% 14%, var(--pink-pale) 0 22%, transparent 23%),
      radial-gradient(circle at 78% 50%, #1A1A2E 0 26%, transparent 27%),
      linear-gradient(180deg, var(--purple-pale) 0%, var(--pink-soft) 35%, var(--blue-mid) 62%, var(--blue-deep) 80%, var(--pink-mid) 100%);
    opacity: 0.85;
    border-radius: 0 0 0 60px;
  }
  .display, .serif, .label, .site { position: absolute; line-height: 1; white-space: nowrap; }
  .display { font-family: "Monoton", "Archivo", sans-serif; color: var(--blue-deep); }
  .serif { font-family: "Abril Fatface", Georgia, serif; color: var(--blue-deep); }
  .title-annual { left: 40px; top: 40px; font-size: 132px; }
  .title-name { left: 40px; top: 206px; font-size: 132px; }
  .event-type { left: 40px; top: 398px; font-size: 56px; }
  .event-meal { left: 40px; top: 452px; font-size: 80px; }
  .event-date { left: 42px; top: 556px; font-size: 38px; }
  .event-time { left: 42px; top: 608px; font-size: 44px; }
  .event-date sup, .rsvp-by sup { font-size: 0.5em; vertical-align: 0.7em; }
  .rsvp-title { left: 40px; top: 722px; font-size: 84px; }
  .rsvp-by { left: 40px; top: 812px; font-size: 34px; color: var(--white); }
  .rule { position: absolute; left: 40px; width: 360px; height: 3px; background: var(--blue-mist); opacity: 0.7; }
  .rule-1 { top: 870px; }
  .rule-2 { top: 958px; }
  .rule-3 { top: 1045px; }
  .label { font-family: "Monoton", "Archivo", sans-serif; color: var(--white); font-size: 50px; left: 42px; }
  .label-place { top: 884px; }
  .label-price { top: 972px; }
  .detail { position: absolute; font-family: "Abril Fatface", Georgia, serif; color: var(--white); line-height: 1.05; }
  .detail-place { left: 264px; top: 886px; font-size: 26px; }
  .detail-place span { display: block; padding-left: 8px; }
  .detail-price { left: 268px; top: 976px; font-size: 30px; }
  .detail-price small { display: block; font-size: 19px; }
  .brand-dot { position: absolute; left: 44px; top: 1094px; width: 80px; height: 80px; border-radius: 50%; background: var(--pink-mist); opacity: 0.85; }
  .site { left: 162px; top: 1112px; font-family: "Archivo", Arial, sans-serif; font-weight: 700; font-size: 48px; color: var(--pink-mist); }
</style>
</head>
<body>
<main class="invite">
  <div class="illustration" role="img" aria-label="Illustration of a 1970s disco dancer in a white suit and flared trousers, with a mirror ball and vinyl records on a lit dance floor"></div>

  <h1>
    <span class="display title-annual">Annual</span>
    <span class="display title-name">MRHT</span>
  </h1>
  <p class="serif event-type">Fundraiser</p>
  <p class="serif event-meal">Dinner</p>
  <p class="serif event-date">October 13<sup>th</sup>, 2022</p>
  <p class="serif event-time">Starts: 6:30pm</p>

  <p class="display rsvp-title">RSVP</p>
  <p class="serif rsvp-by">By September 20<sup>th</sup></p>

  <div class="rule rule-1"></div>
  <p class="label label-place">Place</p>
  <p class="detail detail-place">The<span>Bramwell</span></p>
  <div class="rule rule-2"></div>
  <p class="label label-price">Price</p>
  <p class="detail detail-price">$135<small>per ticket</small></p>
  <div class="rule rule-3"></div>

  <div class="brand-dot"></div>
  <p class="site">MRHT.ORG</p>
</main>
</body>
</html>
```